Lantern

My company name is lantern. The logo is attached. I am the business owner.
Name Gordon Pileck
Phone number- 2018347265
email- Gordon_pileck@mailbrook.net
Website is not live yet but it will be workwithlantern.com
the current beta link is- https://site.qvbtstage.com/lantern-v3/
on the back write “ find creative pros”
Use that beta link as reference for typography and colors on card.

```html
<!DOCTYPE html>
<html lang="en">
<head>
<meta charset="utf-8">
<title>Lantern Business Card</title>
<link rel="stylesheet" href="https://fonts.googleapis.com/css2?family=Open+Sans:ital,wght@0,400;0,700;1,400&display=swap">
<style>
  :root {
    --page-bg: #e9e7e4;
    --card-black: #0d0d0d;
    --accent-orange: #c4501d;
    --text-white: #f2f2f2;
    --text-grey: #b9b9b9;
    --wordmark-grey: #a8a8a8;
  }
  * { box-sizing: border-box; margin: 0; padding: 0; }
  html, body {
    width: 1200px;
    height: 918px;
    overflow: hidden;
    background: var(--page-bg);
    font-family: "Open Sans", Arial, sans-serif;
  }
  .sheet {
    width: 1200px;
    height: 918px;
    display: flex;
    flex-direction: column;
    align-items: center;
    justify-content: center;
    gap: 40px;
  }
  .card {
    position: relative;
    width: 700px;
    height: 400px;
    background: var(--card-black);
    overflow: hidden;
    box-shadow: 0 4px 14px rgba(0, 0, 0, 0.18);
  }
  /* Back side */
  .card-back .frame {
    position: absolute;
    inset: 0;
  }
  .card-back .tagline {
    position: absolute;
    inset: 0;
    display: flex;
    align-items: center;
    justify-content: center;
    font-style: italic;
    font-size: 34px;
    color: var(--text-grey);
    letter-spacing: 0.3px;
  }
  /* Front side */
  .card-front .wordmark {
    position: absolute;
    left: 44px;
    top: 40px;
    font-weight: 700;
    font-size: 58px;
    letter-spacing: 1px;
    color: var(--wordmark-grey);
    line-height: 1;
  }
  .card-front .contact-list {
    position: absolute;
    left: 48px;
    top: 140px;
    list-style: none;
    display: flex;
    flex-direction: column;
    gap: 20px;
  }
  .card-front .contact-item {
    display: flex;
    align-items: center;
    gap: 18px;
    font-size: 27px;
    color: var(--text-white);
    line-height: 1.1;
  }
  .card-front .bullet {
    width: 14px;
    height: 14px;
    background: var(--accent-orange);
    flex: none;
  }
  .card-front .side-band {
    position: absolute;
    right: 40px;
    top: 0;
    width: 22px;
    height: 100%;
    background: var(--accent-orange);
  }
</style>
</head>
<body>
<main class="sheet">
  <section class="card card-back" aria-label="Card back">
    <svg class="frame" width="700" height="400" viewBox="0 0 700 400" aria-hidden="true">
      <polyline points="40,110 40,40 150,40" fill="none" stroke="var(--accent-orange)" stroke-width="14"/>
      <polyline points="550,360 660,360 660,290" fill="none" stroke="var(--accent-orange)" stroke-width="14"/>
    </svg>
    <p class="tagline">“Find creative pros.”</p>
  </section>

  <section class="card card-front" aria-label="Card front">
    <h1 class="wordmark">LANTERN</h1>
    <ul class="contact-list">
      <li class="contact-item"><span class="bullet"></span>Gordon Pileck</li>
      <li class="contact-item"><span class="bullet"></span>201-834-7265</li>
      <li class="contact-item"><span class="bullet"></span>gordon_pileck@mailbrook.net</li>
      <li class="contact-item"><span class="bullet"></span>workwithlantern.com</li>
    </ul>
    <div class="side-band"></div>
  </section>
</main>
</body>
</html>
```